Stationary - Meadowline Homecare
Meadowline Homecare
Professional
Dwayne R Brankett
CEO / President
Street Number / Name
City, State Zip Code
1 (800) XXX-XXXX
1 (555) XXX-XXXX
dbrankett@meadowlinehomecare-example.com
www.meadowlinehomecare-example.com
Please format using concepts from the logo uploaded.
Would like this to stand out as much as possible.
For use of photo on business cards, but im not sure if i want a photo on it or not. I would like to see examples with a photo on it.

```html
<!DOCTYPE html>
<html lang="en">
<head>
<meta charset="utf-8">
<title>Meadowline Homecare – Business Card</title>
<link rel="stylesheet" href="https://fonts.googleapis.com/css2?family=Open+Sans:wght@400;600;700;800&display=swap">
<style>
  :root {
    --page: #ffffff;
    --card-white: #ffffff;
    --brand-red: #c0202f;
    --brand-blue: #2b3a8f;
    --ink: #222222;
    --muted: #555555;
    --photo-top: #cfd6de;
    --photo-bottom: #3b4552;
  }
  * { box-sizing: border-box; margin: 0; padding: 0; }
  html, body {
    width: 1200px; height: 461px; overflow: hidden;
    background: var(--page);
    font-family: "Open Sans", Arial, sans-serif;
  }
  .canvas { position: relative; width: 1200px; height: 461px; }

  .card {
    position: absolute; top: 84px;
    width: 566px; height: 300px;
    border-radius: 22px; overflow: hidden;
    box-shadow: 0 2px 6px rgba(0,0,0,.25);
  }
  .card-front { left: 12px; background: var(--card-white); }
  .card-back { left: 620px; background: var(--brand-red); }

  .front-band { position: absolute; left: 0; bottom: 0; width: 100%; height: 90px; }

  .brand-name {
    font-family: "Open Sans", Arial, sans-serif;
    font-weight: 800; line-height: 1.0; text-transform: uppercase;
    display: flex; align-items: center; gap: 8px;
  }
  .brand-dot { width: 12px; height: 12px; border-radius: 50%; flex: none; }
  .front-brand { position: absolute; left: 16px; top: 20px; color: var(--brand-blue); font-size: 25px; }
  .front-brand .brand-dot { background: var(--brand-red); }

  .person { position: absolute; left: 344px; top: 20px; }
  .person-name { color: var(--brand-blue); font-size: 21px; font-weight: 600; }
  .person-title { color: var(--ink); font-size: 14px; margin-top: 2px; }

  .photo {
    position: absolute; left: 408px; top: 70px; width: 150px; height: 230px;
    background: linear-gradient(180deg, var(--photo-top) 0%, #9aa3ad 45%, var(--photo-bottom) 100%);
  }

  .contact {
    position: absolute; left: 14px; top: 104px;
    font-size: 13.5px; color: var(--ink); line-height: 21px;
  }
  .contact-row { display: flex; }
  .contact-label { width: 72px; }

  .website {
    position: absolute; right: 22px; bottom: 14px;
    color: #fff; font-size: 15px; font-weight: 600;
  }

  .back-brand {
    position: absolute; left: 0; top: 0; width: 100%; height: 100%;
    justify-content: center; color: #fff; font-size: 38px;
  }
  .back-brand .brand-dot { background: #fff; }
</style>
</head>
<body>
<div class="canvas">

  <section class="card card-front">
    <svg class="front-band" viewBox="0 0 566 90" preserveAspectRatio="none" aria-hidden="true">
      <path d="M0 30 C180 60 380 55 566 20 L566 90 L0 90 Z" fill="var(--brand-blue)"/>
      <path d="M0 30 C180 60 380 55 566 20" fill="none" stroke="var(--brand-red)" stroke-width="5"/>
    </svg>

    <div class="brand-name front-brand"><span class="brand-dot"></span>Meadowline<br>Homecare</div>

    <div class="person">
      <div class="person-name">Dwayne R Brankett</div>
      <div class="person-title">CEO / President</div>
    </div>

    <div class="photo" role="img" aria-label="Portrait photo of Dwayne R Brankett in suit and tie"></div>

    <div class="contact">
      <div>Street Number / Name City, State Zip Code</div>
      <div class="contact-row"><span class="contact-label">Toll free</span>: 1 (800) XXX-XXXX</div>
      <div class="contact-row"><span class="contact-label">Phone</span>: 1 (555) XXX-XXXX</div>
      <div class="contact-row"><span class="contact-label">Cell</span>: 1 (555) XXX-XXXX</div>
      <div class="contact-row"><span class="contact-label">Fax</span>: 1 (555) XXX-XXXX</div>
      <div class="contact-row"><span class="contact-label">Email</span>: dbrankett@meadowlinehomecare-example.com</div>
    </div>

    <div class="website">www.meadowlinehomecare-example.com</div>
  </section>

  <section class="card card-back">
    <div class="brand-name back-brand"><span class="brand-dot"></span>Meadowline Homecare</div>
  </section>

</div>
</body>
</html>
```